Website design for an Italian restaurant in Amsterdam

I need a design for a client of mine. It is for Teatro Lunaverde, an Italian restaurant in Amsterdam.
We are going for a clean, modern look but we also need to realise an authentic feel.
The restaurant is located in an old movie theatre, that is where the name Teatro Lunaverde comes from.
Industry/Entity Type
Italian Restaurant
Number of Pages Required
1 page
Font styles to use
Sans Serif
Colors
Designer to choose colors to be used in the design.

```html
<!DOCTYPE html>
<html lang="en">
<head>
<meta charset="utf-8">
<title>Teatro Lunaverde – Italian Restaurant</title>
<link href="https://fonts.googleapis.com/css2?family=Playfair+Display:wght@400;700&family=Open+Sans:wght@400;600&display=swap" rel="stylesheet">
<style>
:root{
  --crimson:#a3354f;
  --crimson-text:#a83a55;
  --black:#0b0b0b;
  --ink:#2e2e2e;
  --text:#555;
  --muted:#777;
  --grey-bg:#f3f3f3;
  --white:#fff;
  --footer:#333335;
  --footer-text:#a9a9a9;
  --line:#c9c9c9;
}
*{box-sizing:border-box;margin:0;padding:0}
html,body{width:1200px;height:2459px;overflow:hidden}
body{position:relative;background:var(--white);font-family:'Playfair Display',Georgia,serif;color:var(--ink)}
.abs{position:absolute}
.center{left:0;width:1200px;text-align:center}

/* top bar */
.topbar{top:0;left:0;width:1200px;height:74px}
.topbar-left{left:0;top:0;width:598px;height:74px;background:var(--black)}
.topbar-right{left:598px;top:0;width:602px;height:74px;background:var(--crimson)}
.brand{left:131px;top:20px;display:flex;align-items:center;gap:12px}
.brand-dot{width:32px;height:32px;border-radius:50%;background:var(--crimson)}
.brand-name{color:var(--white);font-size:19px;letter-spacing:.5px;line-height:1}
.brand-tag{color:var(--crimson);font-size:10px;margin-top:3px;font-family:'Playfair Display',serif}
.phone{left:840px;top:26px;color:var(--white);font-size:16px;display:flex;align-items:center;gap:8px}
.flags{left:1020px;top:30px;display:flex;gap:8px}

/* nav */
.nav{top:74px;height:47px;display:flex;justify-content:center;align-items:center;gap:30px;font-size:12.5px;letter-spacing:.3px}
.nav a{color:var(--ink);text-decoration:none}
.nav a.active{color:var(--crimson-text)}

/* hero */
.hero{top:121px;left:0;width:1200px;height:494px;background:
  radial-gradient(ellipse at 55% 30%,#8a6a3a 0%,rgba(90,60,30,.6) 30%,transparent 60%),
  linear-gradient(180deg,#3a2a1a 0%,#2a1c10 50%,#140c06 100%)}
.hero-title{top:540px;font-size:50px;color:var(--white);letter-spacing:1px;font-weight:700;text-shadow:0 2px 6px rgba(0,0,0,.6)}
.hero-arrow{top:558px}

/* welcome */
.section-title{font-size:34px;color:var(--crimson-text);font-weight:400;letter-spacing:.5px}
.welcome-title{top:686px}
.welcome-sub{top:733px;font-size:17px;color:var(--ink)}
.welcome-text{top:763px;left:131px;width:938px;text-align:center;font-family:'Open Sans',Arial,sans-serif;font-size:12.6px;line-height:22.5px;color:var(--text)}

/* hours */
.grey-menu{top:944px;left:0;width:1200px;height:591px;background:var(--grey-bg)}
.hours-line{top:944px;left:0;width:1200px;height:1px;background:var(--crimson)}
.hours{top:923px;left:411px;width:377px;height:43px;border:1px solid var(--crimson);background:var(--white);display:flex;align-items:center;justify-content:center;gap:14px;color:var(--crimson-text);font-size:16px}
.hours .sep{width:1px;height:20px;background:var(--crimson)}

/* menu */
.menu-title{top:1035px}
.dish{top:1093px;width:301px;height:251px}
.dish-1{left:133px;background:linear-gradient(160deg,#e8e4dc 0%,#7da24a 35%,#d9825a 60%,#f0ede8 100%)}
.dish-2{left:449px;background:linear-gradient(180deg,#3a2414 0%,#5a3218 45%,#e6e0d8 75%,#8a6a50 100%)}
.dish-3{left:767px;background:linear-gradient(150deg,#2a201a 0%,#c58a4e 40%,#9a6232 60%,#241a14 100%)}
.caption{top:1352px;width:301px;text-align:center;font-size:16.5px;color:var(--ink)}
.btn{display:flex;align-items:center;justify-content:center;background:var(--ink);color:var(--white);font-size:15.5px}
.btn-menu{top:1408px;left:523px;width:154px;height:46px}

/* group & reservation */
.col-title{width:500px;text-align:center;font-size:32px;color:var(--crimson-text)}
.col-sub{width:500px;text-align:center;font-size:16.5px;color:var(--ink)}
.btn-group{top:1685px;left:279px;width:154px;height:46px}
.btn-reserve{top:1685px;left:766px;width:154px;height:46px}

/* contact */
.grey-contact{top:1812px;left:0;width:1200px;height:328px;background:var(--grey-bg)}
.contact-title{top:1883px}
.contact-sub{top:1926px;font-size:16.5px;color:var(--ink)}
.field{height:38px;background:var(--white);border:1px solid var(--line);font-family:'Open Sans',Arial,sans-serif;font-size:11.5px;color:var(--muted);display:flex;align-items:center;padding-left:14px}
.f-name{top:1973px;left:133px;width:219px}
.f-email{top:1973px;left:370px;width:220px}
.f-phone{top:1973px;left:608px;width:220px}
.f-date{top:1973px;left:846px;width:221px;justify-content:space-between;padding-right:14px}
.f-msg{top:2029px;left:133px;width:695px}
.btn-submit{top:2029px;left:846px;width:221px;height:38px;font-size:14px;letter-spacing:.5px}

/* footer */
.footer{top:2140px;left:0;width:1200px;height:319px;background:var(--footer)}
.social-box{top:2185px;left:133px;width:934px;height:146px;background:#dcdcdc}
.page-head{top:2195px;left:141px;display:flex;gap:8px}
.page-avatar{width:40px;height:40px;background:#111}
.page-name{font-size:13px;color:var(--ink)}
.page-like{margin-top:5px;display:flex;gap:6px;align-items:center;font-family:'Open Sans',Arial,sans-serif;font-size:10px;color:var(--ink)}
.page-like .like-btn{background:var(--white);border:1px solid #bbb;padding:2px 6px;font-weight:600}
.post{top:2193px;left:339px;width:721px;height:131px;background:var(--white)}
.post-image{top:2193px;left:339px;width:203px;height:131px;background:linear-gradient(135deg,#f2f0ec 0%,#b07a48 50%,#e7a23a 70%,#f2f0ec 100%)}
.post-text{top:2204px;left:559px;font-family:'Open Sans',Arial,sans-serif;font-size:10.5px;line-height:18px;color:#222}
.post-text .link{color:#3a4e8a}
.post-rule{top:2285px;left:559px;width:476px;height:1px;background:#e4e4e4}
.post-actions{top:2295px;left:559px;display:flex;gap:22px;font-family:'Open Sans',Arial,sans-serif;font-size:10px;color:#555;font-weight:600}
.foot-links{top:2372px;left:133px;font-family:'Open Sans',Arial,sans-serif;font-size:11px;color:var(--footer-text);word-spacing:4px}
.copyright{top:2398px;left:133px;font-family:'Open Sans',Arial,sans-serif;font-size:11px;color:var(--footer-text)}
.address{top:2372px;right:220px;text-align:right;font-family:'Open Sans',Arial,sans-serif;font-size:11px;color:var(--footer-text);line-height:26px}
.social-dot{top:2378px;width:33px;height:33px;border-radius:50%;background:#555}
</style>
</head>
<body>

<header>
  <div class="abs topbar-left"></div>
  <div class="abs topbar-right"></div>
  <div class="abs brand">
    <span class="brand-dot"></span>
    <div>
      <div class="brand-name">TEATRO LUNAVERDE</div>
      <div class="brand-tag">Ristorante Italiano</div>
    </div>
  </div>
  <div class="abs phone">
    <svg width="14" height="14" viewBox="0 0 24 24"><path fill="#fff" d="M6.6 10.8a15 15 0 0 0 6.6 6.6l2.2-2.2c.3-.3.7-.4 1-.2 1.1.4 2.3.6 3.6.6.6 0 1 .4 1 1V20c0 .6-.4 1-1 1A17 17 0 0 1 3 4c0-.6.4-1 1-1h3.5c.6 0 1 .4 1 1 0 1.3.2 2.5.6 3.6.1.3 0 .7-.2 1z"/></svg>
    (+31) 20 555 0148
  </div>
  <div class="abs flags">
    <svg width="18" height="12" viewBox="0 0 18 12" aria-label="English">
      <rect width="18" height="12" fill="#24337a"/>
      <path d="M0 0L18 12M18 0L0 12" stroke="#fff" stroke-width="2.4"/>
      <path d="M0 0L18 12M18 0L0 12" stroke="#c8102e" stroke-width="0.9"/>
      <path d="M9 0V12M0 6H18" stroke="#fff" stroke-width="3.6"/>
      <path d="M9 0V12M0 6H18" stroke="#c8102e" stroke-width="2"/>
    </svg>
    <svg width="18" height="12" viewBox="0 0 18 12" aria-label="Nederlands">
      <rect width="18" height="4" fill="#ae1c28"/>
      <rect y="4" width="18" height="4" fill="#fff"/>
      <rect y="8" width="18" height="4" fill="#21468b"/>
    </svg>
  </div>
</header>

<nav class="abs center nav">
  <a class="active" href="#">HOME</a>
  <a href="#">MENU</a>
  <a href="#">GROUPMENU</a>
  <a href="#">RESERVATION</a>
  <a href="#">CONTACT</a>
</nav>

<section>
  <div class="abs hero" role="img" aria-label="Warmly lit restaurant interior in an old cinema, with string lights, set tables and a film projected on the wall"></div>
  <h1 class="abs center hero-title">AUTHENTIC ITALIAN CUISINE</h1>
  <svg class="abs hero-arrow" style="left:54px" width="22" height="32" viewBox="0 0 22 32"><path d="M16 4L6 16l10 12" fill="none" stroke="#fff" stroke-width="4"/></svg>
  <svg class="abs hero-arrow" style="left:1124px" width="22" height="32" viewBox="0 0 22 32"><path d="M6 4l10 12L6 28" fill="none" stroke="#fff" stroke-width="4"/></svg>
</section>

<section>
  <h2 class="abs center section-title welcome-title">WELCOME TO TEATRO LUNAVERDE</h2>
  <p class="abs center welcome-sub">Italian Restaurant</p>
  <p class="abs welcome-text">Fusce nec leo ac urna pulvinar auctor. Mauris bibendum fringilla velit. Nulla in lorem at massa pellentesque posuere. Nulla tristique posuere molestie. Aliquam erat volutpat. Etiam quis aliquet risus. Duis ornare erat eget magna dapibus, in accumsan quam pharetra. Nam tempus, quam in bibendum vulputate, sapien dolor viverra nisl, vitae euismod elit turpis et nulla. Aliquam erat volutpat. Pellentesque blandit lacus eget nunc faucibus, et tincidunt eros viverra. Phasellus consequat sagittis nisi suscipit feugiat. Cras eget leo sed nunc hendrerit ultricies eu at nisl. Praesent iaculis faucibus urna sit amet lacinia.</p>
</section>

<section>
  <div class="abs grey-menu"></div>
  <div class="abs hours-line"></div>
  <div class="abs hours"><span>Tue - Sun &nbsp;- &nbsp;18:00 - 23:00</span><span class="sep"></span><span>Monday Closed</span></div>
  <h2 class="abs center section-title menu-title">TODAY ON OUR MENU</h2>
  <div class="abs dish dish-1" role="img" aria-label="Grilled fish fillet on green asparagus with cherry tomatoes"></div>
  <div class="abs dish dish-2" role="img" aria-label="Beef fillet plated with gnocchi beside a glass of red wine"></div>
  <div class="abs dish dish-3" role="img" aria-label="Grilled dish on a dark wooden board with roasted garlic"></div>
  <p class="abs caption" style="left:133px">Orata al Pistacchio</p>
  <p class="abs caption" style="left:449px">Filetto di Manzo al Gorgonzola e Noci</p>
  <p class="abs caption" style="left:767px">Melanzana alla Parmigiana</p>
  <a class="abs btn btn-menu">View Full Menu</a>
</section>

<section>
  <h2 class="abs col-title" style="left:106px;top:1606px">GROUPMENU</h2>
  <p class="abs col-sub" style="left:106px;top:1650px">We serve groupmenus for reservations for 10 guests or more</p>
  <a class="abs btn btn-group">View Groupmenu</a>
  <h2 class="abs col-title" style="left:593px;top:1606px">RESERVATION</h2>
  <p class="abs col-sub" style="left:593px;top:1650px">Tables can be reserved online through our website</p>
  <a class="abs btn btn-reserve">Reserve Now</a>
</section>

<section>
  <div class="abs grey-contact"></div>
  <h2 class="abs center section-title contact-title">CONTACT</h2>
  <p class="abs center contact-sub">For all your questions you can use our contact form</p>
  <div class="abs field f-name">Name</div>
  <div class="abs field f-email">Email</div>
  <div class="abs field f-phone">Phone</div>
  <div class="abs field f-date">Date and Time <svg width="10" height="6" viewBox="0 0 10 6"><path d="M0 0h10L5 6z" fill="#666"/></svg></div>
  <div class="abs field f-msg">Message</div>
  <a class="abs btn btn-submit">SUBMIT</a>
</section>

<footer>
  <div class="abs footer"></div>
  <div class="abs social-box"></div>
  <div class="abs page-head">
    <div class="page-avatar"></div>
    <div>
      <div class="page-name">Teatro Lunaverde</div>
      <div class="page-like"><span class="like-btn">Like Page</span><span>2.3K likes</span></div>
    </div>
  </div>
  <div class="abs post"></div>
  <div class="abs post-image" role="img" aria-label="Plated meat dish with golden sauce on a white plate"></div>
  <div class="abs post-text">Nuovo Teatro Lunaverde<br>New chef, great authentic italian food<br>Getting hungry yet?<br><span class="link">www.teatrolunaverde.info</span></div>
  <div class="abs post-rule"></div>
  <div class="abs post-actions"><span>▲ 12</span><span>Comment</span><span>➦ Share</span></div>

  <p class="abs foot-links">Home &nbsp;| &nbsp;Menu &nbsp;| &nbsp;Groupmenu &nbsp;| &nbsp;Reservation &nbsp;| &nbsp;Contact</p>
  <p class="abs copyright">Copyright © &nbsp;2018 &nbsp;Teatro Lunaverde. &nbsp;All rights reserved.</p>
  <p class="abs address">Lindengracht 42, 1015KL Amsterdam<br>Tel nr: (+31) 20 555 0148</p>
  <span class="abs social-dot" style="left:991px"></span>
  <span class="abs social-dot" style="left:1033px"></span>
</footer>

</body>
</html>
```